Vask Christmas Postcard

I would like a postcard I can send to potential clients for the Christmas Holiday. It should include my services as well as industries serviced but be geared towards the holiday season.

```html
<!DOCTYPE html>
<html lang="en">
<head>
<meta charset="utf-8">
<title>Vask Christmas Postcard</title>
<link href="https://fonts.googleapis.com/css2?family=Montserrat:wght@500;600;700;800;900&family=Great+Vibes&display=swap" rel="stylesheet">
<style>
:root{
  --backdrop:#8a8b8f;
  --navy:#1d2a6b;
  --navy-deep:#141d52;
  --sky:#2aa7e6;
  --sky-light:#7fd0f7;
  --ink:#121418;
  --white:#ffffff;
  --hat-red:#c92a2a;
  --line:#cfd3d8;
}
*{box-sizing:border-box;margin:0;padding:0}
html,body{width:1200px;height:3060px;overflow:hidden}
body{background:var(--backdrop);font-family:'Montserrat',Arial,sans-serif;position:relative}
.card{position:absolute;left:60px;width:1080px;height:720px;overflow:hidden;box-shadow:0 10px 30px rgba(0,0,0,.25)}
.card--front{top:640px;background:radial-gradient(ellipse at 50% 40%,#2a3a86 0%,var(--navy) 55%,var(--navy-deep) 100%)}
.card--back{top:1640px;background:var(--white)}

/* front */
.front__trees{position:absolute;left:0;right:0;bottom:0;height:150px;background:linear-gradient(to top,#10184a,rgba(16,24,74,0))}
.front__shield{position:absolute;left:270px;top:22px;width:540px;height:680px}
.front__hat-area{position:absolute;left:282px;top:30px;width:110px;height:80px;border-radius:8px;background:linear-gradient(180deg,var(--hat-red),#a51f1f)}
.front__content{position:absolute;left:300px;top:110px;width:480px;text-align:center;color:var(--white)}
.brand{display:inline-flex;align-items:center;gap:10px}
.brand__dot{width:22px;height:22px;border-radius:50%;background:var(--sky)}
.brand__name{font-weight:900;font-size:44px;letter-spacing:1px;color:var(--white)}
.brand__tag{font-size:10px;font-weight:600;letter-spacing:3px;margin-top:2px}
.front__script{font-family:'Great Vibes',cursive;font-size:88px;color:var(--sky-light);line-height:1;margin-top:30px}
.front__title{font-weight:900;font-size:84px;line-height:1;letter-spacing:0;white-space:nowrap}
.pill{display:inline-block;background:var(--sky);color:var(--white);font-weight:800;border-radius:8px}
.front__offer{font-size:30px;padding:10px 30px;margin-top:16px;letter-spacing:1px}
.front__cta{font-size:13px;font-weight:700;letter-spacing:1.5px;margin-top:30px}
.front__phone{font-size:17px;padding:7px 22px;margin-top:10px}

/* back */
.back__panel{position:absolute;left:0;top:0;width:560px;height:720px;background:var(--ink);color:var(--white)}
.back__bar{height:66px;background:var(--sky);display:flex;align-items:center;justify-content:flex-end;padding-right:34px;gap:12px}
.back__bar-script{font-family:'Great Vibes',cursive;font-size:34px}
.back__bar-title{font-weight:900;font-size:32px;letter-spacing:1px}
.services{display:grid;grid-template-columns:1fr 1fr;gap:22px 20px;padding:30px 30px 0}
.service{display:flex;align-items:center;gap:12px;font-size:16px;font-weight:600;line-height:1.2}
.service svg{flex:none}
.back__lower{display:flex;margin-top:28px}
.industries{width:290px;background:var(--navy);padding:20px 26px;height:370px}
.industries__title{font-weight:800;font-size:17px;letter-spacing:1px;margin-bottom:16px}
.industries li{list-style:none;display:flex;align-items:center;gap:10px;font-size:16px;font-weight:600;margin-bottom:14px}
.industries li::before{content:"";width:9px;height:9px;border-radius:50%;background:var(--sky);flex:none}
.industries li.is-script{font-family:'Great Vibes',cursive;font-size:26px;font-weight:400;color:var(--sky-light)}
.season{flex:1;text-align:center;padding-top:30px}
.season__badge{width:140px;height:160px;margin:0 auto;border-radius:20px 20px 70px 70px;background:linear-gradient(160deg,#2b3b86,#0d1340);border:5px solid var(--white)}
.season__title{font-weight:800;font-size:19px;margin-top:18px;letter-spacing:1px}
.season__phone{font-size:15px;padding:6px 16px;margin-top:10px}
.season__web{font-size:12px;font-weight:600;margin-top:10px;letter-spacing:1px}
.back__brand{position:absolute;left:620px;top:46px;display:flex;align-items:center;gap:10px}
.back__brand .brand__name{color:var(--navy);font-size:40px}
.back__brand .brand__tag{color:var(--navy)}
.stamp{position:absolute;right:40px;top:36px;width:110px;height:130px;border:2px solid var(--line);background:#f4f5f7}
.address{position:absolute;left:620px;right:40px;top:420px}
.address span{display:block;height:2px;background:var(--line);margin-bottom:56px}
</style>
</head>
<body>

<section class="card card--front" aria-label="Postcard front">
  <div class="front__trees" role="img" aria-label="Faint winter pine tree silhouettes"></div>
  <svg class="front__shield" viewBox="0 0 540 680" aria-hidden="true">
    <path d="M270 18 C350 60 440 70 514 62 L514 330 C514 500 400 600 270 660 C140 600 26 500 26 330 L26 62 C100 70 190 60 270 18 Z" fill="rgba(20,29,82,.35)" stroke="#ffffff" stroke-width="24" stroke-linejoin="round"/>
  </svg>
  <div class="front__hat-area" role="img" aria-label="Santa hat illustration resting on the shield corner"></div>
  <div class="front__content">
    <div class="brand"><span class="brand__dot"></span><span class="brand__name">VASK</span></div>
    <div class="brand__tag">SECURITY &amp; PROTECTION</div>
    <div class="front__script">Christmas</div>
    <div class="front__title">HOLIDAY</div>
    <div class="pill front__offer">SERVICES OFFER</div>
    <div class="front__cta">CONTACT OUR EXPERTS TODAY</div>
    <div class="pill front__phone">555-014-2290</div>
  </div>
</section>

<section class="card card--back" aria-label="Postcard back">
  <div class="back__panel">
    <div class="back__bar"><span class="back__bar-script">Our Priority</span><span class="back__bar-title">SERVICES</span></div>
    <div class="services">
      <div class="service"><svg width="30" height="34" viewBox="0 0 30 34"><path d="M15 2 L28 7 V16 C28 25 22 30 15 32 C8 30 2 25 2 16 V7 Z" fill="none" stroke="#2aa7e6" stroke-width="3"/><path d="M9 17 L13 21 L21 12" fill="none" stroke="#fff" stroke-width="3"/></svg>Mobile<br>Patrol</div>
      <div class="service"><svg width="30" height="34" viewBox="0 0 30 34"><path d="M15 2 L28 7 V16 C28 25 22 30 15 32 C8 30 2 25 2 16 V7 Z" fill="none" stroke="#2aa7e6" stroke-width="3"/><path d="M9 17 L13 21 L21 12" fill="none" stroke="#fff" stroke-width="3"/></svg>Property<br>Checks</div>
      <div class="service"><svg width="30" height="34" viewBox="0 0 30 34"><path d="M15 2 L28 7 V16 C28 25 22 30 15 32 C8 30 2 25 2 16 V7 Z" fill="none" stroke="#2aa7e6" stroke-width="3"/><path d="M9 17 L13 21 L21 12" fill="none" stroke="#fff" stroke-width="3"/></svg>Alarm<br>Response</div>
      <div class="service"><svg width="30" height="34" viewBox="0 0 30 34"><path d="M15 2 L28 7 V16 C28 25 22 30 15 32 C8 30 2 25 2 16 V7 Z" fill="none" stroke="#2aa7e6" stroke-width="3"/><path d="M9 17 L13 21 L21 12" fill="none" stroke="#fff" stroke-width="3"/></svg>Emergency<br>Services</div>
      <div class="service"><svg width="30" height="34" viewBox="0 0 30 34"><path d="M15 2 L28 7 V16 C28 25 22 30 15 32 C8 30 2 25 2 16 V7 Z" fill="none" stroke="#2aa7e6" stroke-width="3"/><path d="M9 17 L13 21 L21 12" fill="none" stroke="#fff" stroke-width="3"/></svg>Fire<br>Watch</div>
      <div class="service"><svg width="30" height="34" viewBox="0 0 30 34"><path d="M15 2 L28 7 V16 C28 25 22 30 15 32 C8 30 2 25 2 16 V7 Z" fill="none" stroke="#2aa7e6" stroke-width="3"/><path d="M9 17 L13 21 L21 12" fill="none" stroke="#fff" stroke-width="3"/></svg>Permanent &amp; Temporary<br>Security Services</div>
    </div>
    <div class="back__lower">
      <div class="industries">
        <div class="industries__title">INDUSTRIES WE SERVE</div>
        <ul>
          <li>Construction</li>
          <li>Logistics</li>
          <li>Warehouses</li>
          <li>Marijuana<br>Facilities</li>
          <li class="is-script">Church/ Synagogue</li>
        </ul>
      </div>
      <div class="season">
        <div class="season__badge" role="img" aria-label="Shield badge with a security guard illustration"></div>
        <div class="season__title">HOLIDAY SEASON</div>
        <div class="pill season__phone">555-014-2290</div>
        <div class="season__web">WWW.VASKSECURITY.COM</div>
      </div>
    </div>
  </div>
  <div class="back__brand">
    <span class="brand__dot"></span>
    <div><div class="brand__name">VASK</div><div class="brand__tag">SECURITY &amp; PROTECTION</div></div>
  </div>
  <div class="stamp"></div>
  <div class="address"><span></span><span></span><span></span><span></span></div>
</section>

</body>
</html>
```